Harbormile Trade Associates - Letterhead and Folder

I am looking for letterhead that uses the splash from the logo on the side of the page as well as some information from our website.

I am looking for a folder that is a fold out that has pockets to hold paper as well as a slits for a business card.

Website address is www.harbormiletradeassociates.example

Target Market(s)

Export of Agrifoods, commodities and emergency aid.
Supplying the world food security.

Requirements
Must have
• Use splash and logo, have information about company.
• Letterhead must have splash on a side not in the middle.
Nice to have
• Different pictures that what are provided.

```html
<!DOCTYPE html>
<html lang="en">
<head>
<meta charset="utf-8">
<title>Harbormile Trade Associates – Letterhead and Folder</title>
<link rel="stylesheet" href="https://fonts.googleapis.com/css2?family=Arimo:wght@400;700&family=Open+Sans:wght@400;600;700&display=swap">
<style>
  :root{
    --bg:#ececec;
    --paper:#ffffff;
    --green:#4aa33d;
    --green-dark:#2f8a35;
    --lime:#a8c93a;
    --teal:#1f8a9a;
    --ink:#222222;
    --muted:#666666;
    --blue-name:#3b7fc4;
    --faint:#e3efdf;
    --photo-a:#3f74c4;
    --photo-b:#9fbf4e;
  }
  *{margin:0;padding:0;box-sizing:border-box}
  html,body{width:1200px;height:1000px;overflow:hidden;background:var(--bg)}
  body{position:relative;font-family:"Arimo",Arial,sans-serif;color:var(--ink)}
  .sheet{position:absolute;background:var(--paper);overflow:hidden}

  /* Letterhead */
  .letterhead{left:40px;top:175px;width:462px;height:652px}
  .brand{position:absolute;z-index:2;display:flex;align-items:center;gap:8px;font-family:"Open Sans",Arial,sans-serif;font-weight:700;color:var(--green-dark)}
  .brand-dot{border-radius:50%;background:var(--green);flex:none}
  .letterhead .brand{left:40px;top:27px;font-size:14px}
  .letterhead .brand-dot{width:40px;height:40px}
  .sender{position:absolute;left:323px;top:28px;font-style:normal;font-family:"Open Sans",Arial,sans-serif;font-size:7px;line-height:11px;color:var(--muted)}
  .sender strong{color:#444}
  .letter{position:absolute;z-index:2;left:40px;top:131px;width:410px;font-size:8.6px;line-height:12px;color:var(--ink)}
  .letter p{margin-bottom:12px}
  .signature{width:80px;height:24px;margin:4px 0 2px;background:#f1f1f1}
  .signer{color:var(--blue-name);font-size:8.6px}
  .faint-ring{position:absolute;z-index:0;border-radius:50%;border:10px solid var(--faint)}
  .letterhead .faint-ring{left:272px;top:440px;width:160px;height:160px}
  .swoosh{position:absolute;z-index:1;left:0;bottom:0}
  .web{position:absolute;z-index:3;right:50px;bottom:13px;font-family:"Open Sans",Arial,sans-serif;font-size:8px;color:#fff}

  /* Folder outside */
  .folder-outside{left:544px;top:53px;width:622px;height:440px}
  .fold-line{position:absolute;left:311px;top:0;width:1px;height:100%;background:#eee}
  .photo{position:absolute;left:311px;top:0;width:311px;height:340px;background:linear-gradient(160deg,var(--photo-a),var(--photo-b))}
  .folder-outside .photo-curve{position:absolute;z-index:1;left:311px;top:300px}
  .folder-outside .faint-ring{left:150px;top:283px;width:162px;height:162px}
  .brand-back{left:82px;top:362px;font-size:10px}
  .brand-back .brand-dot{width:32px;height:32px}
  .brand-front{left:353px;top:364px;font-size:16px}
  .brand-front .brand-dot{width:58px;height:58px}
  .social{position:absolute;z-index:2;left:132px;top:411px;display:flex;gap:6px}
  .social span{width:12px;height:12px;background:var(--teal);border-radius:2px}

  /* Folder inside */
  .folder-inside{left:547px;top:525px;width:622px;height:437px}
  .pockets{position:absolute;left:0;top:0}
  .about{position:absolute;left:18px;top:326px;width:240px;color:#fff;font-family:"Open Sans",Arial,sans-serif}
  .about h2{font-size:9px;font-weight:700;margin-bottom:4px}
  .about p{font-size:4.6px;line-height:7px}
  .card-slot{position:absolute;left:418px;top:332px;width:125px;height:83px;border:1px dashed #fff;color:#fff;font-family:"Open Sans",Arial,sans-serif;font-size:11px;display:flex;align-items:center;justify-content:center}
</style>
</head>
<body>

<section class="sheet letterhead" aria-label="Letterhead">
  <div class="brand"><span class="brand-dot"></span>Harbormile Trade Associates</div>
  <address class="sender">
    <strong>Harbormile Trade Associates Ltd.</strong><br>
    418 Quayside Row<br>Port Aldern, NR<br>K4T9B2
  </address>

  <div class="faint-ring" aria-hidden="true"></div>

  <div class="letter">
    <p>9 September, 2016</p>
    <p>Mr. Morgan Vale<br>President<br>Harbormile Trade Associates<br>111 Street Name, Suite#<br>City State, 12345</p>
    <p>Dear Mr. Morgan,</p>
    <p>Lorem ipsum dolor sit amet, cu augue evertitur definitiones per, eum impetus tamquam dissentiet in. Enim sensibus ullamcorper mel ei, sit accumsan dissentias ad, usu cu fugit melius prodesset. Ea mei ancillae mandamus salutatus. Has ad sumo prima, eam in illum dissentiet, no sale graeci pro. Noster iuvaret moderatius no per.</p>
    <p>Movet soluta semper has te, graece cetero intellegat usu id. Everti meliore et vel, cu mea idque utroque nostrum. Cu ius lorem constituam, alii debet percipit vix at. Modus altera sea ei, vix dico constituto te. Cu eam nibh putent, est soluta reformidans eu. Esse nominavi vim ad, ne populo evertitur conceptam per.</p>
    <p>Usu zril facilisis laboramus eu, pro harum ancillae scripserit ad, pro in zril vocibus graecis. Duo id elit vocent, id nobis aperiam luptatum per. Est illum mediocrem reprehendunt ea, ius ut novum mazim deleniti. Et eos possit temporibus, erroribus referrentur et est. Usu purto virtute consetetur ea, ne pri novum mazim prompta.</p>
    <p>Nisl natum dicta usu no, sea id vidit forensibus, nec an prompta periculis. Eam id veniam accusata. Nulla adolescens constituam an his. Dolore constituam ex sea. Te pri commodo feugait laboramus, qui petentium consectetuer ea, an duo falli ridens graeco. Mei verear nostrud discere ei, postea noluisse honestatis eam eu.</p>
    <p style="margin-bottom:0">Sincerely Yours,</p>
    <div class="signature" role="img" aria-label="Handwritten signature"></div>
    <div class="signer">MORGAN VALE</div>
  </div>

  <svg class="swoosh" width="462" height="46" viewBox="0 0 462 46" aria-hidden="true">
    <path d="M60 46 C190 14 340 4 462 6 V46 Z" fill="var(--lime)"/>
    <path d="M140 46 C250 16 360 9 462 10 V46 Z" fill="#fff"/>
    <path d="M155 46 C260 19 365 12 462 13 V46 Z" fill="var(--green)"/>
  </svg>
  <div class="web">www.harbormiletradeassociates.example</div>
</section>

<section class="sheet folder-outside" aria-label="Presentation folder, outside">
  <div class="fold-line"></div>
  <div class="faint-ring" aria-hidden="true"></div>
  <div class="photo" role="img" aria-label="Photo of a country road between flowering crop fields under a cloudy sky"></div>
  <svg class="photo-curve" width="311" height="60" viewBox="0 0 311 60" aria-hidden="true">
    <path d="M0 40 C90 52 200 44 311 12 V60 H0 Z" fill="var(--lime)"/>
    <path d="M0 44 C90 56 200 48 311 18 V60 H0 Z" fill="var(--green)"/>
    <path d="M0 48 C90 60 200 54 311 26 V60 H0 Z" fill="#fff"/>
  </svg>
  <div class="brand brand-back"><span class="brand-dot"></span>Harbormile Trade Associates</div>
  <div class="social" aria-label="Social links"><span></span><span></span></div>
  <div class="brand brand-front"><span class="brand-dot"></span>Harbormile Trade<br>Associates</div>
</section>

<section class="sheet folder-inside" aria-label="Presentation folder, inside">
  <svg class="pockets" width="622" height="437" viewBox="0 0 622 437" aria-hidden="true">
    <path d="M0 313 H254 C280 313 292 330 292 350 C292 380 296 410 300 437 H0 Z" fill="var(--green)"/>
    <path d="M322 437 C326 405 330 372 338 350 C346 326 360 313 380 313 H622 V437 Z" fill="var(--green)"/>
    <line x1="412" y1="346" x2="436" y2="326" stroke="#fff" stroke-width="1"/>
    <line x1="526" y1="420" x2="550" y2="400" stroke="#fff" stroke-width="1"/>
  </svg>
  <div class="about">
    <h2>About Us</h2>
    <p>Harbormile Trade Associates is a broker and supplier of grains, oilseeds, food products and emergency aid for global markets. We connect growers and buyers to move quality commodities across borders, backed by a skilled team in trade, logistics and legal matters. We build lasting partnerships with producers and buyers, helping supply world food security with care, speed and fair dealing in every market we serve.</p>
  </div>
  <div class="card-slot">85mm x 55mm</div>
</section>

</body>
</html>
```